LUPO Baby Massage Classes - flyer to make a difference

I need a single page flyer, preferably single page, to hand out to doctors, medical centres and parents. To also leave on counters of establishments.
It is to promote my baby massage classes. Mums can get together with other mums and book a 5 week course to learn and discover the many benefits of baby massage.
Benefits include: enhances bonding and attachment, understand non-verbal cues from your baby, helps with sleep patterns, help with immune system, increases vagal activity,relief from wind, colic or constipation to name some.

Baby age from birth to 12 months. Group classes or private sessions

I am a Professional Member and Certified by the Global Guild of Cradle Touch (GGCT) GGCT Australia is Nationally Accredited and is endorsed by Crestfield Board of Carers, the Southvale Council of Birthworkers, The Westbrook Society of Daily Living Practice Oceania, The Harbourline Union of Bodywork Practitioner and is a full member of Kindred Wellbeing Network.

Class detail and availability contact is Carol Perkins 0478 315 027 carol.jean.perkins@examplemail.net www.lupocradletouch com.au facebook/comLUPOcradletouch

My colour scheme is green and purple as you will see from my logo and website. I would like my flyer to be softer tones of either both colours or just one.

I will include some images you can choose from or show me any you think will fit in with baby massage. THANK YOU
Updates

Hi The size of my flyer is A6. Approx 150mms x 210mms and single sided. Thank you

Target Market(s)

mums and dads, groups, doctors, midwives

Industry/Entity Type

Medical

Font styles to use
Sans Serif

Colors
87d0c7
b09cc8

Requirements
Must have
• baby photo or photos, both my logo and the GGCT logo. The GGCT logo is to be small
• Baby Massage Classes (wording) is very important to catch the eye.
• Invitation to book a class or gather friends to book is next in importance
• Benefits is next
• The admin information ie.,membership, certification and endorsements are lesser and can be small.
• Contact information to be noticeable.
Nice to have
• If you have an idea, drawing or photo that would look better, please feel free to try it
Should not have
• should not be crowded with information all the same size

```html
<!DOCTYPE html>
<html lang="en">
<head>
<meta charset="utf-8">
<title>LUPO Baby Massage Classes</title>
<link rel="stylesheet" href="https://fonts.googleapis.com/css2?family=Open+Sans:ital,wght@0,400;0,600;0,700;1,300;1,400;1,600;1,700&display=swap">
<style>
  :root {
    --teal: #14a898;
    --teal-deep: #0f9a8b;
    --purple: #8a2f8c;
    --purple-soft: #9b5aa0;
    --white: #ffffff;
    --rule: rgba(255,255,255,0.45);
    --skin-light: #f4e6df;
    --skin-mid: #e7c9bb;
    --sheet: #eef0f2;
  }
  * { margin: 0; padding: 0; box-sizing: border-box; }
  html, body { width: 848px; height: 1200px; overflow: hidden; background: var(--white); }
  body { font-family: "Open Sans", Arial, sans-serif; }

  .flyer { position: relative; width: 848px; height: 1200px; overflow: hidden; background: var(--teal); color: var(--white); }

  .hero-photo {
    position: absolute; left: 0; top: 0; width: 848px; height: 780px;
    background:
      radial-gradient(ellipse 260px 300px at 300px 260px, #f6dccd 0%, rgba(246,220,205,0) 100%),
      radial-gradient(ellipse 320px 260px at 620px 320px, var(--skin-mid) 0%, rgba(231,201,187,0) 100%),
      linear-gradient(160deg, var(--sheet) 0%, var(--skin-light) 55%, #ece4e2 100%);
  }

  .wave { position: absolute; left: 0; top: 0; width: 848px; height: 1200px; }

  .brand-tab {
    position: absolute; left: 584px; top: 0; width: 212px; height: 140px;
    background: var(--white); border-radius: 0 0 14px 14px;
    display: flex; align-items: center; justify-content: center; gap: 12px;
    box-shadow: 0 2px 6px rgba(0,0,0,0.08);
  }
  .brand-tab .dot { width: 44px; height: 44px; border-radius: 50%; background: var(--teal); }
  .brand-tab .name { font-weight: 700; font-size: 40px; color: var(--purple); letter-spacing: 1px; }

  .guild-mark {
    position: absolute; left: 342px; top: 640px; width: 96px;
    text-align: center; font-weight: 600; font-size: 20px; color: var(--purple-soft); letter-spacing: 1px;
  }

  .instructor { position: absolute; left: 468px; top: 480px; width: 220px; text-align: center; }
  .instructor .portrait {
    width: 220px; height: 220px; border-radius: 50%; background: var(--teal);
    display: flex; align-items: center; justify-content: center;
  }
  .instructor .portrait-ring {
    width: 196px; height: 196px; border-radius: 50%; background: var(--white);
    display: flex; align-items: center; justify-content: center;
  }
  .instructor .portrait-photo {
    width: 176px; height: 176px; border-radius: 50%;
    background: linear-gradient(180deg, #4d6b3c 0%, #7a8f5c 45%, #b79ab8 80%, #8e5aa0 100%);
  }
  .instructor .name { margin-top: 2px; font-style: italic; font-weight: 700; font-size: 18px; color: var(--white); }

  .headline {
    position: absolute; left: 0; top: 748px; width: 848px; text-align: center;
    font-style: italic; font-weight: 300; font-size: 66px; line-height: 1; color: var(--white);
  }
  .headline strong { font-weight: 600; }

  .rule { position: absolute; left: 35px; width: 778px; height: 1px; background: var(--rule); }
  .rule.top { top: 846px; }
  .rule.bottom { top: 972px; }

  .benefits {
    position: absolute; left: 40px; top: 866px; width: 768px; text-align: center;
    font-size: 18px; line-height: 25px; color: var(--white);
  }

  .cta {
    position: absolute; left: 44px; top: 1000px; width: 768px; height: 82px;
    background: var(--purple); border: 4px solid var(--white); border-radius: 42px;
    display: flex; align-items: center;
  }
  .cta svg { margin-left: 40px; }
  .cta .label { margin-left: 28px; font-style: italic; font-weight: 700; font-size: 31px; color: var(--white); }

  .contact {
    position: absolute; left: 0; top: 1094px; width: 848px; text-align: center;
    font-style: italic; font-size: 24px; line-height: 32px; color: var(--white);
  }
  .contact .sep { margin: 0 14px; }
</style>
</head>
<body>
<main class="flyer">
  <div class="hero-photo" role="img" aria-label="Photo of a smiling baby lying on a white sheet while a parent's hands massage its chest"></div>

  <svg class="wave" viewBox="0 0 848 1200" aria-hidden="true">
    <path fill="var(--teal)" d="M0 760 C40 700 70 600 90 470 C100 400 115 345 150 342 C185 340 200 400 215 470 C225 510 300 500 430 522 C330 540 270 560 290 640 C310 700 380 720 460 700 C470 560 690 560 700 680 C760 680 810 660 848 650 L848 1200 L0 1200 Z"/>
  </svg>

  <div class="brand-tab">
    <span class="dot"></span>
    <span class="name">LUPO</span>
  </div>

  <div class="guild-mark">GGCT</div>

  <div class="instructor">
    <div class="portrait">
      <div class="portrait-ring">
        <div class="portrait-photo" role="img" aria-label="Portrait photo of instructor Carol Perkins"></div>
      </div>
    </div>
    <p class="name">Carol Perkins</p>
  </div>

  <h1 class="headline">Baby <strong>Massage</strong> Classes</h1>

  <div class="rule top"></div>
  <p class="benefits">Benefits include: enhances bonding and attachment, understand non-verbal cues from your baby, helps with sleep patterns, help with immune system, increases vagal activity,relief from wind, colic or constipation to name some.</p>
  <div class="rule bottom"></div>

  <div class="cta">
    <svg width="44" height="58" viewBox="0 0 44 58" aria-hidden="true">
      <path fill="var(--white)" d="M22 2 C32 12 34 26 31 40 L13 40 C10 26 12 12 22 2 Z"/>
      <circle cx="22" cy="20" r="5" fill="var(--purple)"/>
      <path fill="var(--white)" d="M12 30 L4 44 L13 42 Z M32 30 L40 44 L31 42 Z"/>
      <rect x="15" y="44" width="4" height="8" fill="var(--white)"/>
      <rect x="25" y="44" width="4" height="8" fill="var(--white)"/>
    </svg>
    <span class="label">book a class or gather friends to book</span>
  </div>

  <address class="contact">
    0478 315 027<br>
    carol.jean.perkins@examplemail.net<span class="sep">|</span>www.lupocradletouch com.au<br>
    facebook/comLUPOcradletouch
  </address>
</main>
</body>
</html>
```